Velter Labs - Mushroom Supplement Packaging

Our brand is called Velter Labs. I've added a couple different logos that you can use. We are creating a line up of Mushroom Supplement products. I will add the entire line-up of products here. I've added examples of other products and packaging shape types I can purchase. Give me different options for packaging that is minimalist and clean for this brand that makes it look really well made and clean and make people want to buy.

Product 1 Lions Mane 1g
Product 2 Cordyceps 1g
Product 3 Chaga 1g
Product 4 Turkey Tail 1g
Product 5 Reishi 1g
Product 6 Maitake 1g
Product 7 Shiitake 1g

Product 8 (Mix) Lions Mane 143mg
Cordyceps 143mg
Chaga 143mg
Turkey Tail 143mg
Reishi 143mg
Maitake 143mg
Shiitake 143mg

```html
<!DOCTYPE html>
<html lang="en">
<head>
<meta charset="utf-8">
<title>Velter Labs – Mushroom Supplement Labels</title>
<link rel="stylesheet" href="https://fonts.googleapis.com/css2?family=Saira+Extra+Condensed:wght@500;600&family=Saira:wght@500;700&family=Saira+Condensed:wght@500;600&family=Rubik:wght@300;400;500&display=swap">
<style>
  :root {
    --page-bg: #ececed;
    --label-bg: #ffffff;
    --ink-dark: #2b2f34;
    --ink-text: #33373c;
    --blue-mid: #2f8ad8;
    --blue-light: #55a9ea;
    --purple-mid: #7e3590;
    --purple-light: #a24bb6;
    --illustration-grey: #d9dadc;
  }
  * { box-sizing: border-box; margin: 0; padding: 0; }
  html, body { width: 1200px; height: 778px; overflow: hidden; }
  body { background: var(--page-bg); position: relative; }

  .label {
    position: absolute;
    top: 75px;
    width: 480px;
    height: 628px;
    background: var(--label-bg);
    overflow: hidden;
    box-shadow: 0 6px 18px rgba(0,0,0,0.10);
  }
  .label--lions-mane { left: 90px; --accent-mid: var(--blue-mid); --accent-light: var(--blue-light); }
  .label--turkey-tail { left: 630px; --accent-mid: var(--purple-mid); --accent-light: var(--purple-light); }

  .label__art { position: absolute; left: 0; top: 0; width: 480px; height: 628px; }

  .type-condensed { font-family: "Saira Extra Condensed", "Arial Narrow", sans-serif; font-weight: 500; }
  .type-condensed-bold { font-family: "Saira Extra Condensed", "Arial Narrow", sans-serif; font-weight: 600; }
  .type-heavy { font-family: "Saira", sans-serif; font-weight: 700; }
  .type-semi { font-family: "Saira Condensed", "Arial Narrow", sans-serif; font-weight: 600; }
  .type-regular { font-family: "Saira Condensed", "Arial Narrow", sans-serif; font-weight: 500; }

  .benefits {
    position: absolute; left: 49px; top: 420px; width: 385px;
    font-family: "Rubik", sans-serif; font-weight: 400;
    font-size: 15px; color: var(--ink-text); white-space: nowrap;
  }
  .benefits strong { font-weight: 500; }

  .origin {
    position: absolute; left: 49px; top: 465px; width: 207px; height: 67px;
    border-top: 1px dashed var(--accent-mid);
    border-bottom: 1px dashed var(--accent-mid);
    padding-top: 13px;
    font-family: "Rubik", sans-serif; font-weight: 300; font-size: 12px; line-height: 1.35;
    color: var(--ink-text); white-space: nowrap;
  }
  .origin strong { font-weight: 500; }

  .mushroom-art {
    position: absolute; left: 280px; top: 458px; width: 150px; height: 110px;
    background: radial-gradient(ellipse at 50% 60%, #f1f1f2 0%, var(--illustration-grey) 75%);
    border-radius: 50% 50% 8px 8px / 70% 70% 8px 8px;
  }
</style>
</head>
<body>

<section class="label label--lions-mane">
  <svg class="label__art" viewBox="0 0 480 628" aria-hidden="false">
    <defs>
      <linearGradient id="domeBlue" x1="0" y1="0" x2="1" y2="0">
        <stop offset="0" stop-color="#1d72c9"/><stop offset="1" stop-color="#4fa6e8"/>
      </linearGradient>
      <linearGradient id="nameBlue" x1="0" y1="0" x2="0" y2="1">
        <stop offset="0" stop-color="#2e86d6"/><stop offset="0.5" stop-color="#2a7fd2"/><stop offset="1" stop-color="#1462bd"/>
      </linearGradient>
    </defs>
    <path d="M0 0 H480 V110 Q240 230 0 110 Z" fill="url(#domeBlue)"/>
    <text class="type-condensed" x="145" y="106" font-size="66" fill="#fff" textLength="190" lengthAdjust="spacingAndGlyphs">VELTER</text>
    <text class="type-condensed" x="175" y="137" font-size="30" fill="#fff" textLength="130" lengthAdjust="spacingAndGlyphs">LABS</text>

    <text class="type-condensed" x="52" y="282" font-size="124" fill="url(#nameBlue)" textLength="375" lengthAdjust="spacingAndGlyphs">LION’S MANE</text>
    <text class="type-heavy" x="52" y="351" font-size="74" fill="#2b2f34" textLength="375" lengthAdjust="spacingAndGlyphs">MUSHROOM</text>

    <rect x="49" y="366" width="377" height="38" rx="5" fill="#2b2f34"/>
    <path d="M54 366 H205 V404 H54 Q49 404 49 399 V371 Q49 366 54 366 Z" fill="#55a9ea"/>
    <text class="type-condensed-bold" x="57" y="395" font-size="27" fill="#fff" textLength="140" lengthAdjust="spacingAndGlyphs">EXTRA STRENGTH</text>
    <text class="type-regular" x="221" y="392" font-size="19" fill="#fff" textLength="195" lengthAdjust="spacingAndGlyphs">Organic Mushroom Extract</text>

    <path d="M49 628 V570 Q49 560 59 560 H138 Q148 560 148 570 V628 Z" fill="#55a9ea"/>
    <text class="type-heavy" x="57" y="604" font-size="26" fill="#fff" textLength="82" lengthAdjust="spacingAndGlyphs">143MG</text>
    <text class="type-semi" x="165" y="600" font-size="17" fill="#2b2f34" textLength="255" lengthAdjust="spacingAndGlyphs">120 CAPSULES | DIETARY SUPPLEMENT</text>
    <path d="M148 628 V621 H440 Q452 621 458 612 L466 602 H480 V628 Z" fill="#2f8ad8"/>
  </svg>
  <p class="benefits">Immunity System <strong>Support, Energy &amp; Clarity*</strong></p>
  <p class="origin">Made with <strong>100 % Organic<br>Lion’s Mane Mushroom</strong></p>
  <div class="mushroom-art" role="img" aria-label="Line illustration of a lion's mane mushroom"></div>
</section>

<section class="label label--turkey-tail">
  <svg class="label__art" viewBox="0 0 480 628">
    <defs>
      <linearGradient id="domePurple" x1="0" y1="0" x2="1" y2="0">
        <stop offset="0" stop-color="#6a2a7e"/><stop offset="1" stop-color="#9a45ad"/>
      </linearGradient>
      <linearGradient id="namePurple" x1="0" y1="0" x2="0" y2="1">
        <stop offset="0" stop-color="#7d3490"/><stop offset="0.5" stop-color="#6b2a80"/><stop offset="1" stop-color="#55206a"/>
      </linearGradient>
    </defs>
    <path d="M0 0 H480 V110 Q240 230 0 110 Z" fill="url(#domePurple)"/>
    <text class="type-condensed" x="145" y="106" font-size="66" fill="#fff" textLength="190" lengthAdjust="spacingAndGlyphs">VELTER</text>
    <text class="type-condensed" x="175" y="137" font-size="30" fill="#fff" textLength="130" lengthAdjust="spacingAndGlyphs">LABS</text>

    <text class="type-condensed" x="52" y="282" font-size="124" fill="url(#namePurple)" textLength="375" lengthAdjust="spacingAndGlyphs">TURKEY TAIL</text>
    <text class="type-heavy" x="52" y="351" font-size="74" fill="#2b2f34" textLength="375" lengthAdjust="spacingAndGlyphs">MUSHROOM</text>

    <rect x="49" y="366" width="377" height="38" rx="5" fill="#2b2f34"/>
    <path d="M54 366 H205 V404 H54 Q49 404 49 399 V371 Q49 366 54 366 Z" fill="#a24bb6"/>
    <text class="type-condensed-bold" x="57" y="395" font-size="27" fill="#fff" textLength="140" lengthAdjust="spacingAndGlyphs">EXTRA STRENGTH</text>
    <text class="type-regular" x="221" y="392" font-size="19" fill="#fff" textLength="195" lengthAdjust="spacingAndGlyphs">Organic Mushroom Extract</text>

    <path d="M49 628 V570 Q49 560 59 560 H138 Q148 560 148 570 V628 Z" fill="#a24bb6"/>
    <text class="type-heavy" x="57" y="604" font-size="26" fill="#fff" textLength="82" lengthAdjust="spacingAndGlyphs">143MG</text>
    <text class="type-semi" x="165" y="600" font-size="17" fill="#2b2f34" textLength="255" lengthAdjust="spacingAndGlyphs">120 CAPSULES | DIETARY SUPPLEMENT</text>
    <path d="M148 628 V621 H440 Q452 621 458 612 L466 602 H480 V628 Z" fill="#7e3590"/>
  </svg>
  <p class="benefits">Immunity System <strong>Support, Energy &amp; Clarity*</strong></p>
  <p class="origin">Made with <strong>100 % Organic<br>Turkey Tail Mushroom</strong></p>
  <div class="mushroom-art" role="img" aria-label="Line illustration of a turkey tail mushroom"></div>
</section>

</body>
</html>
```